Business Card Design Project

I am community manager and social media strategist. I need a double sided business card with company logo and name. Looking for something professional, elegant but also a little bit original.

• - The logo and the colours are the company colours and a required to stay.
- The size should be: 84 x 55 mm (or 3.30 x 2.16)
- The file size should be: 1039 x 697 pixels (300 dpi)
- I'd like rounded corners. :)

Use the following contact information for the card:

Léonie Vardin
Stratégie médias sociaux / community management / édition de sites sociaux
mob. : 0687529103
leonie.vardin@postelune.fr
Twitter. : @lvardin
Skype : vardin.leonie

```html
<!DOCTYPE html>
<html lang="fr">
<head>
<meta charset="utf-8">
<title>Carte de visite – Léonie Vardin</title>
<link rel="stylesheet" href="https://fonts.googleapis.com/css2?family=Tinos:wght@400;700&display=swap">
<style>
  :root {
    --backdrop: #000000;
    --accent: #1b5e9e;
    --ink: #111111;
    --label: #ffffff;
    --watermark: rgba(90, 90, 90, 0.25);
    --grad-teal: #64c2d9;
    --grad-lime: #c8d84a;
    --grad-orange: #f7b56a;
    --grad-ice: #b7dde9;
  }
  * { margin: 0; padding: 0; box-sizing: border-box; }
  html, body {
    width: 1200px;
    height: 1108px;
    overflow: hidden;
    background: var(--backdrop);
  }
  .sheet {
    position: relative;
    width: 1200px;
    height: 1108px;
  }
  .card {
    position: absolute;
    border-radius: 38px;
    overflow: hidden;
    background: linear-gradient(90deg,
      var(--grad-teal) 0%,
      var(--grad-lime) 32%,
      var(--grad-orange) 66%,
      var(--grad-ice) 100%);
  }
  .card--front { left: 31px; top: 35px; width: 740px; height: 480px; }
  .card--back  { left: 437px; top: 537px; width: 740px; height: 484px; }

  .brand {
    position: absolute;
    display: flex;
    flex-direction: column;
    align-items: center;
  }
  .brand__dot {
    border-radius: 50%;
    background: var(--accent);
  }
  .brand__name {
    font-family: "Tinos", "Times New Roman", serif;
    font-weight: 700;
    color: var(--ink);
    line-height: 1;
  }

  .card--front .brand { left: 0; right: 0; top: 50px; }
  .card--front .brand__dot { width: 230px; height: 230px; }
  .card--front .brand__name { font-size: 104px; margin-top: 44px; }

  .brand--standalone-right { left: 850px; top: 155px; width: 310px; }
  .brand--standalone-right .brand__dot { width: 120px; height: 120px; }
  .brand--standalone-right .brand__name { font-size: 56px; margin-top: 32px; color: var(--label); }

  .brand--standalone-left { left: 48px; top: 770px; width: 310px; }
  .brand--standalone-left .brand__dot { width: 130px; height: 130px; }
  .brand--standalone-left .brand__name { font-size: 58px; margin-top: 36px; color: var(--label); }

  .watermark-dot {
    position: absolute;
    left: 330px;
    top: 150px;
    width: 150px;
    height: 150px;
    border-radius: 50%;
    background: var(--watermark);
  }
  .watermark-name {
    position: absolute;
    left: 290px;
    top: 362px;
    width: 430px;
    text-align: right;
    font-family: "Tinos", "Times New Roman", serif;
    font-weight: 700;
    font-size: 84px;
    line-height: 1;
    color: var(--watermark);
  }

  .holder-name {
    position: absolute;
    left: 38px;
    top: 70px;
    font-family: "Tinos", "Times New Roman", serif;
    font-weight: 700;
    font-size: 66px;
    color: var(--ink);
    line-height: 1;
  }
  .contact {
    position: absolute;
    left: 25px;
    top: 314px;
    list-style: none;
    font-family: "Tinos", "Times New Roman", serif;
    font-size: 21px;
    line-height: 26.5px;
    color: var(--ink);
  }

  .side-label {
    position: absolute;
    font-family: "Tinos", "Times New Roman", serif;
    font-size: 50px;
    color: var(--label);
    line-height: 1;
  }
  .side-label--front { left: 155px; top: 530px; }
  .side-label--back  { left: 735px; top: 1035px; }
</style>
</head>
<body>
<main class="sheet">

  <section class="card card--front" aria-label="Recto">
    <div class="brand">
      <span class="brand__dot"></span>
      <span class="brand__name">VENTALIS</span>
    </div>
  </section>
  <p class="side-label side-label--front">Front</p>

  <div class="brand brand--standalone-right">
    <span class="brand__dot"></span>
    <span class="brand__name">VENTALIS</span>
  </div>

  <div class="brand brand--standalone-left">
    <span class="brand__dot"></span>
    <span class="brand__name">VENTALIS</span>
  </div>

  <section class="card card--back" aria-label="Verso">
    <span class="watermark-dot" aria-hidden="true"></span>
    <span class="watermark-name" aria-hidden="true">VENTALIS</span>
    <h1 class="holder-name">Léonie Vardin</h1>
    <ul class="contact">
      <li>Stratégie médias sociaux / community management / édition de sites sociaux</li>
      <li>mob. : 0687529103</li>
      <li>leonie.vardin@postelune.fr</li>
      <li>Twitter. : @lvardin</li>
      <li>Skype : vardin.leonie</li>
    </ul>
  </section>
  <p class="side-label side-label--back">Back</p>

</main>
</body>
</html>
```